Business card design needed

New company in Executive Search & Consulting (Recruitment & Head Hunting Company)

We recruit IT, Accounting & Finance, Human Resources and Senior Management

with offices in Perth, Brisbane, Seoul and Hong Kong

Industry/Entity Type

Business

Contact Information for Business Card

Calderwood-Ashfield Executive Search & Consulting
*Perth *Brisbane * Seoul * Hong Kong
Neil Calderwood Australian Director
147 Mellor Street Subiaco Western Australia
www.calderwoodashfield.example.au
Ph: 08 6000 4827 Fax: 08 6000 9153
Mobile: 0400 731 562

```html
<!DOCTYPE html>
<html lang="en">
<head>
<meta charset="utf-8">
<title>Calderwood-Ashfield Business Card</title>
<link rel="stylesheet" href="https://fonts.googleapis.com/css2?family=Crimson+Text:wght@400;600;700&display=swap">
<style>
  :root {
    --backdrop: #d9d9d9;
    --card-top: #ffffff;
    --card-bottom: #e4e4e4;
    --ink: #2a2a2a;
    --ink-soft: #555555;
    --logo-ink: #6f747a;
    --steel-light: #f2f3f4;
    --steel-mid: #a9adb2;
    --steel-dark: #4c5056;
  }
  * { box-sizing: border-box; margin: 0; padding: 0; }
  html, body {
    width: 1200px; height: 900px; overflow: hidden;
    background: var(--backdrop);
    font-family: "Crimson Text", "Times New Roman", serif;
    color: var(--ink);
  }
  .canvas { position: relative; width: 1200px; height: 900px; }
  .card {
    position: absolute; left: 250px; width: 700px; height: 400px;
    border-radius: 28px; overflow: hidden;
    background: linear-gradient(160deg, var(--card-top) 0%, var(--card-bottom) 100%);
    box-shadow: 0 6px 18px rgba(0,0,0,0.18);
  }
  .card--front { top: 40px; }
  .card--back { top: 465px; }
  .puzzle-art { position: absolute; inset: 0; width: 100%; height: 100%; }

  .brand { display: flex; align-items: center; gap: 12px; position: absolute; }
  .brand__mark { width: 14px; height: 14px; background: var(--logo-ink); }
  .brand__name {
    font-weight: 400; color: var(--logo-ink); letter-spacing: 0.06em;
    text-transform: uppercase; line-height: 1.1;
  }
  .card--front .brand { left: 70px; top: 170px; }
  .card--front .brand__name { font-size: 28px; }
  .card--front .brand__tagline {
    position: absolute; left: 96px; top: 212px;
    font-size: 15px; letter-spacing: 0.14em; text-transform: uppercase; color: var(--logo-ink);
  }

  .card--back .brand { right: 36px; top: 30px; }
  .card--back .brand__name { font-size: 16px; }
  .back-company {
    position: absolute; right: 36px; top: 52px; text-align: right;
    font-size: 11px; letter-spacing: 0.1em; text-transform: uppercase; color: var(--logo-ink);
  }
  .offices {
    position: absolute; right: 36px; top: 76px; text-align: right;
    font-size: 16px; color: var(--ink);
  }
  .website {
    position: absolute; right: 36px; top: 100px; text-align: right;
    font-size: 16px; font-weight: 600; color: var(--ink);
  }

  .person { position: absolute; left: 190px; top: 118px; }
  .person__name { font-size: 24px; font-weight: 700; }
  .person__title { font-size: 16px; font-weight: 600; color: var(--ink-soft); }

  .contacts { position: absolute; left: 36px; top: 236px; list-style: none; }
  .contacts li { display: flex; align-items: center; gap: 10px; font-size: 20px; line-height: 1.25; }
  .contacts svg { width: 14px; height: 16px; fill: var(--ink); }
  .address {
    position: absolute; left: 36px; bottom: 34px;
    display: flex; align-items: center; gap: 10px; font-size: 21px;
  }
  .address svg { width: 18px; height: 16px; fill: var(--ink); }
</style>
</head>
<body>
<main class="canvas">

  <section class="card card--front" aria-label="Card front">
    <svg class="puzzle-art" viewBox="0 0 700 400" role="img" aria-label="Diagonal band of brushed-steel puzzle pieces">
      <defs>
        <linearGradient id="steel-band" x1="0" y1="0" x2="1" y2="1">
          <stop offset="0" stop-color="var(--steel-light)"/>
          <stop offset="0.45" stop-color="var(--steel-mid)"/>
          <stop offset="0.7" stop-color="var(--steel-dark)"/>
          <stop offset="1" stop-color="var(--steel-mid)"/>
        </linearGradient>
      </defs>
      <polygon points="560,0 700,0 700,130 500,400 330,400" fill="url(#steel-band)"/>
    </svg>
    <div class="brand">
      <span class="brand__mark"></span>
      <span class="brand__name">Calderwood-Ashfield</span>
    </div>
    <div class="brand__tagline">Executive Search &amp; Consulting</div>
  </section>

  <section class="card card--back" aria-label="Card back">
    <svg class="puzzle-art" viewBox="0 0 700 400" role="img" aria-label="Clusters of brushed-steel puzzle pieces in the top-left and right corners">
      <defs>
        <linearGradient id="steel-corner" x1="0" y1="0" x2="1" y2="1">
          <stop offset="0" stop-color="var(--steel-light)"/>
          <stop offset="0.5" stop-color="var(--steel-mid)"/>
          <stop offset="1" stop-color="var(--steel-dark)"/>
        </linearGradient>
      </defs>
      <polygon points="0,0 180,0 180,40 110,40 110,90 60,90 60,170 0,170" fill="url(#steel-corner)"/>
      <polygon points="640,130 700,130 700,330 560,330 560,290 610,290 610,200 640,200" fill="url(#steel-corner)"/>
    </svg>

    <div class="brand">
      <span class="brand__mark"></span>
      <span class="brand__name">Calderwood-Ashfield</span>
    </div>
    <div class="back-company">Executive Search &amp; Consulting</div>
    <div class="offices">Perth - Brisbane - Seoul - Hong Kong</div>
    <div class="website">www.calderwoodashfield.example.au</div>

    <div class="person">
      <div class="person__name">Neil Calderwood</div>
      <div class="person__title">Australian Director</div>
    </div>

    <ul class="contacts">
      <li>
        <svg viewBox="0 0 14 16" aria-hidden="true"><path d="M3 0h8a1 1 0 0 1 1 1v14a1 1 0 0 1-1 1H3a1 1 0 0 1-1-1V1a1 1 0 0 1 1-1zm0 2v10h8V2zm4 11a1 1 0 1 0 0 2 1 1 0 0 0 0-2z"/></svg>
        <span>0400 731 562</span>
      </li>
      <li>
        <svg viewBox="0 0 14 16" aria-hidden="true"><path d="M3 2l3 3-1.5 2a9 9 0 0 0 4 4L10.5 9.5l3 3L12 15C6 15 0 9 0 3z"/></svg>
        <span>08 6000 4827</span>
      </li>
      <li>
        <svg viewBox="0 0 14 16" aria-hidden="true"><path d="M3 1h7v4H3zM1 6h12v7h-2v2H3v-2H1zm3 5v3h6v-3z"/></svg>
        <span>08 6000 9153</span>
      </li>
    </ul>

    <div class="address">
      <svg viewBox="0 0 18 16" aria-hidden="true"><path d="M9 0l9 8h-3v8h-4v-5H7v5H3V8H0z"/></svg>
      <span>147 Mellor Street Subiaco Western Australia</span>
    </div>
  </section>

</main>
</body>
</html>
```